New to ArtHarbor? This contest is for you!

Are you new to ArtHarbor and looking to enter your first contest? Look no further!

Requirements:
* We want you to create a beautiful and eye-catching graphic design for your ArtHarbor PROFILE PIC
* Upload your design to this contest and to your profile
* You must upload your entry before 12:00am 1 May AEST
* You must be new to ArtHarbor (registered in April) to be eligible

Conditions of Entry:
* This contest is only open to designers who opened their account this month (April 2015)
* You should only submit 1 design to this contest
* Your design must adhere to our quality standards to be eligible to receive a prize

Prizes:
* First prize for the best design is $150
* Second prize is $100
* Up to 150 x $5 participation payments ($750) available to be awarded to high-quality designs

Requirements
Must have
• An original design, created by you.
Should not have
• Your design should not be a copy of another design, or contain any generic elements or overused design concepts.

```html
<!DOCTYPE html>
<html lang="en">
<head>
<meta charset="utf-8">
<title>K.Rahim — Web Design &amp; Branding</title>
<link rel="stylesheet" href="https://fonts.googleapis.com/css2?family=Raleway:wght@300;400&family=Alfa+Slab+One&display=swap">
<style>
  :root {
    --accent: #fcc62d;
    --slate-dark: #3c3d4a;
    --slate-mid: #54566a;
    --band-grey: #a6a6ae;
    --band-grey-dark: #98989f;
    --paper: #ffffff;
    --paper-shade: #f3f3f3;
    --ice: #dfeef5;
    --ink: #111111;
    --white: #ffffff;
  }
  html, body {
    margin: 0;
    padding: 0;
    width: 1200px;
    height: 1000px;
    overflow: hidden;
    background: var(--paper);
  }
  .canvas {
    position: relative;
    width: 1200px;
    height: 1000px;
    overflow: hidden;
    font-family: "Raleway", sans-serif;
  }
  .top-rule {
    position: absolute;
    top: 0; left: 0;
    width: 100%; height: 4px;
    background: var(--accent);
    z-index: 3;
  }
  .hero-backdrop {
    position: absolute;
    top: 0; left: 0;
    width: 100%; height: 522px;
    background: radial-gradient(ellipse at 85% 10%, #6a6c80 0%, var(--slate-mid) 35%, var(--slate-dark) 100%);
  }
  .scallop-edge {
    position: absolute;
    top: 514px; left: 0;
    width: 1200px; height: 14px;
    z-index: 2;
  }
  .grey-band {
    position: absolute;
    top: 520px; left: 0;
    width: 100%; height: 112px;
    background: linear-gradient(to bottom, var(--band-grey-dark), var(--band-grey));
  }
  .torn-edge {
    position: absolute;
    top: 618px; left: 0;
    width: 1200px; height: 20px;
    z-index: 2;
  }
  .paper-backdrop {
    position: absolute;
    top: 630px; left: 0;
    width: 100%; height: 370px;
    background: linear-gradient(to bottom, var(--paper), var(--paper-shade));
  }
  .brand-mark {
    position: absolute;
    top: 160px; left: 0;
    width: 100%;
    display: flex;
    align-items: center;
    justify-content: center;
    gap: 14px;
    z-index: 4;
  }
  .brand-mark-dot {
    width: 18px;
    height: 18px;
    border-radius: 50%;
    background: var(--accent);
  }
  .brand-mark-name {
    color: var(--white);
    font-family: "Raleway", sans-serif;
    font-weight: 400;
    font-size: 44px;
    line-height: 60px;
    letter-spacing: 2px;
  }
  .brand-name {
    position: absolute;
    top: 318px; left: 0;
    width: 100%;
    text-align: center;
    margin: 0;
    font-family: "Alfa Slab One", serif;
    font-weight: 400;
    font-size: 80px;
    line-height: 1.15;
    letter-spacing: 1px;
    color: var(--accent);
    z-index: 4;
  }
  .brand-tagline {
    position: absolute;
    top: 414px; left: 0;
    width: 100%;
    text-align: center;
    margin: 0;
    font-family: "Raleway", sans-serif;
    font-weight: 400;
    font-size: 27px;
    letter-spacing: 4px;
    color: var(--ice);
    z-index: 4;
  }
  .site-address {
    position: absolute;
    top: 780px; left: 0;
    width: 100%;
    text-align: center;
    margin: 0;
    font-family: "Raleway", sans-serif;
    font-weight: 300;
    font-size: 58px;
    color: var(--ink);
    z-index: 4;
  }
  .site-address-highlight {
    display: inline-block;
    background: var(--accent);
    color: var(--white);
    padding: 0 10px;
    margin: 0 4px 0 10px;
    line-height: 62px;
  }
</style>
</head>
<body>
<main class="canvas">
  <div class="top-rule"></div>

  <div class="hero-backdrop" role="img" aria-label="Dark slate textured background covered in a faint pattern of hand-drawn school doodles"></div>

  <svg class="scallop-edge" viewBox="0 0 1200 14" preserveAspectRatio="none" aria-hidden="true">
    <path d="M0 4 Q6 12 12 4 Q18 12 24 4 Q30 12 36 4 Q42 12 48 4 Q54 12 60 4 Q66 12 72 4 Q78 12 84 4 Q90 12 96 4 Q102 12 108 4 Q114 12 120 4 Q126 12 132 4 Q138 12 144 4 Q150 12 156 4 Q162 12 168 4 Q174 12 180 4 Q186 12 192 4 Q198 12 204 4 Q210 12 216 4 Q222 12 228 4 Q234 12 240 4 Q246 12 252 4 Q258 12 264 4 Q270 12 276 4 Q282 12 288 4 Q294 12 300 4 Q306 12 312 4 Q318 12 324 4 Q330 12 336 4 Q342 12 348 4 Q354 12 360 4 Q366 12 372 4 Q378 12 384 4 Q390 12 396 4 Q402 12 408 4 Q414 12 420 4 Q426 12 432 4 Q438 12 444 4 Q450 12 456 4 Q462 12 468 4 Q474 12 480 4 Q486 12 492 4 Q498 12 504 4 Q510 12 516 4 Q522 12 528 4 Q534 12 540 4 Q546 12 552 4 Q558 12 564 4 Q570 12 576 4 Q582 12 588 4 Q594 12 600 4 Q606 12 612 4 Q618 12 624 4 Q630 12 636 4 Q642 12 648 4 Q654 12 660 4 Q666 12 672 4 Q678 12 684 4 Q690 12 696 4 Q702 12 708 4 Q714 12 720 4 Q726 12 732 4 Q738 12 744 4 Q750 12 756 4 Q762 12 768 4 Q774 12 780 4 Q786 12 792 4 Q798 12 804 4 Q810 12 816 4 Q822 12 828 4 Q834 12 840 4 Q846 12 852 4 Q858 12 864 4 Q870 12 876 4 Q882 12 888 4 Q894 12 900 4 Q906 12 912 4 Q918 12 924 4 Q930 12 936 4 Q942 12 948 4 Q954 12 960 4 Q966 12 972 4 Q978 12 984 4 Q990 12 996 4 Q1002 12 1008 4 Q1014 12 1020 4 Q1026 12 1032 4 Q1038 12 1044 4 Q1050 12 1056 4 Q1062 12 1068 4 Q1074 12 1080 4 Q1086 12 1092 4 Q1098 12 1104 4 Q1110 12 1116 4 Q1122 12 1128 4 Q1134 12 1140 4 Q1146 12 1152 4 Q1158 12 1164 4 Q1170 12 1176 4 Q1182 12 1188 4 Q1194 12 1200 4" fill="none" stroke="#d6ebf2" stroke-width="2"/>
  </svg>

  <div class="grey-band"></div>

  <svg class="torn-edge" viewBox="0 0 1200 20" preserveAspectRatio="none" aria-hidden="true">
    <path d="M0 12 L30 9 L55 14 L80 8 L110 13 L140 10 L170 15 L200 9 L235 12 L260 8 L295 14 L330 10 L360 13 L390 7 L420 12 L455 9 L485 14 L515 10 L545 13 L575 8 L610 12 L640 9 L670 14 L700 10 L735 13 L760 8 L795 12 L825 10 L855 15 L885 9 L915 12 L950 8 L980 13 L1010 10 L1040 14 L1070 9 L1100 12 L1130 8 L1165 13 L1200 10 L1200 20 L0 20 Z" fill="#ffffff"/>
  </svg>

  <div class="paper-backdrop" role="img" aria-label="White paper background with a faint pattern of light grey school doodles"></div>

  <div class="brand-mark">
    <span class="brand-mark-dot"></span>
    <span class="brand-mark-name">K.RAHIM</span>
  </div>

  <h1 class="brand-name">K.RAHIM</h1>
  <p class="brand-tagline">WEB DESIGN &amp; BRANDING</p>

  <p class="site-address">www.<span class="site-address-highlight">krahim</span>.com</p>
</main>
</body>
</html>
```